Book cover (front only) for proposal by established author

We need a book cover design - must be inspirational, credible, powerful, noticeable - for a self-help book being written by an established author (15 books with major publishers). Front cover only. This will be used in a proposal being sent to a literary agent; it's NOT for publication, so high-res is NOT needed. We are providing a draft design in a doc format, but you have complete freedom with the graphics, colors, and fonts. Final product should be a pdf file, unless you have a better suggestion.

```html
<!DOCTYPE html>
<html lang="en">
<head>
<meta charset="UTF-8">
<title>What We Can Be — Book Cover</title>
<link rel="stylesheet" href="https://fonts.googleapis.com/css2?family=Open+Sans:wght@400;700;800&family=Tinos:wght@400;700&display=swap">
<style>
  :root {
    --paper: #f1f1ef;
    --paper-shade: #e6e6e3;
    --navy: #0d2a66;
    --red: #e3130f;
    --rule: #e2954a;
    --mark-grey: #d6d6d4;
    --sun-light: #fbe27a;
    --sun-mid: #f7c63a;
    --sun-edge: #f39a1e;
  }
  * { margin: 0; padding: 0; box-sizing: border-box; }
  html, body { width: 849px; height: 1200px; overflow: hidden; background: var(--paper); }
  .cover {
    position: relative;
    width: 849px;
    height: 1200px;
    overflow: hidden;
    background: radial-gradient(ellipse at 50% 40%, var(--paper) 55%, var(--paper-shade) 100%);
    font-family: "Open Sans", Arial, sans-serif;
  }
  .title-question {
    position: absolute;
    left: 680px;
    top: 95px;
    font-family: "Tinos", "Times New Roman", serif;
    font-size: 250px;
    line-height: 1;
    color: var(--mark-grey);
  }
  .title {
    position: absolute;
    top: 72px;
    left: 0;
    width: 100%;
    text-align: center;
  }
  .title-top {
    display: block;
    font-weight: 800;
    font-size: 134px;
    line-height: 1;
    letter-spacing: 2px;
    color: var(--navy);
  }
  .title-bottom {
    display: block;
    margin-top: 2px;
    font-weight: 400;
    font-size: 108px;
    line-height: 1;
    color: var(--red);
  }
  .rule {
    position: absolute;
    left: 82px;
    width: 685px;
    border-top: 2px dashed var(--rule);
  }
  .rule-top { top: 332px; }
  .rule-bottom { top: 512px; }
  .benefits {
    position: absolute;
    top: 360px;
    left: 0;
    width: 100%;
    text-align: center;
    list-style: none;
    font-weight: 700;
    font-size: 23px;
    line-height: 44px;
    color: var(--red);
  }
  .benefits .dot {
    display: inline-block;
    width: 15px;
    height: 15px;
    margin: 0 8px;
    border-radius: 50%;
    background: var(--navy);
    vertical-align: 1px;
  }
  .emblem {
    position: absolute;
    left: 234px;
    top: 581px;
    width: 380px;
    height: 380px;
  }
  .tagline {
    position: absolute;
    top: 1004px;
    left: 0;
    width: 100%;
    text-align: center;
    font-family: "Tinos", "Times New Roman", serif;
    font-size: 24px;
    line-height: 31px;
    color: var(--navy);
  }
  .author-band {
    position: absolute;
    left: 0;
    bottom: 0;
    width: 100%;
    height: 113px;
    background: var(--navy);
    display: flex;
    align-items: center;
    justify-content: center;
  }
  .author-name {
    font-family: "Tinos", "Times New Roman", serif;
    font-size: 42px;
    letter-spacing: 1px;
    color: #ffffff;
  }
  .author-name .credential { font-weight: 700; }
</style>
</head>
<body>
  <div class="cover">
    <span class="title-question" aria-hidden="true">?</span>
    <h1 class="title">
      <span class="title-top">WHAT</span>
      <span class="title-bottom">WE CAN BE</span>
    </h1>

    <div class="rule rule-top"></div>
    <ul class="benefits">
      <li>HAPPIER IN OUR RELATIONSHIPS<span class="dot"></span>BETTER PARENTS</li>
      <li>MORE FIT<span class="dot"></span>MORE CREATIVE<span class="dot"></span>MORE MOTIVATED</li>
      <li>MORE CALM<span class="dot"></span>AND MORE SEXUALLY FULFILLED</li>
    </ul>
    <div class="rule rule-bottom"></div>

    <svg class="emblem" viewBox="0 0 380 380" role="img" aria-label="Smiling emoji with heart eyes">
      <defs>
        <radialGradient id="sun-fill" cx="45%" cy="35%" r="70%">
          <stop offset="0%" stop-color="var(--sun-light)"/>
          <stop offset="70%" stop-color="var(--sun-mid)"/>
          <stop offset="100%" stop-color="var(--sun-edge)"/>
        </radialGradient>
      </defs>
      <circle cx="190" cy="190" r="184" fill="url(#sun-fill)" stroke="var(--sun-edge)" stroke-width="8"/>
    </svg>

    <p class="tagline">America’s leading research psychologist shows the potential<br>we all have to feel and function better in every aspect of our lives</p>

    <div class="author-band">
      <p class="author-name">DANIEL MARLOWE - <span class="credential">PH.D.</span></p>
    </div>
  </div>
</body>
</html>
```